Cover for CD-single

TOVA is a young singer-songwriter and needs a CD cover design for her first single "Stars over harbour". Her song is about her best friend who recently moved from Europe to Australia with her family. But even though they now live on the other side of the world, they will always be there for each other.
You can use the picture attached or you can see it as an inspiration.
Please put the name of the artist: TOVA
and the name of the song on the cover: Stars over harbour

```html
<!DOCTYPE html>
<html lang="en">
<head>
<meta charset="utf-8">
<title>TOVA – Stars over harbour – CD single cover</title>
<link rel="stylesheet" href="https://fonts.googleapis.com/css2?family=Nunito+Sans:wght@400&display=swap">
<style>
  :root {
    --page: #ffffff;
    --ink-light: #fbf8f4;
    --sky: #e6cfd0;
    --forest-high: #8a5a48;
    --forest-mid: #6e3a27;
    --hair-glow: #b5562a;
    --road: #b79a95;
    --cloud: #d9d9ef;
    --cloud-bright: #eceaf7;
    --shadow: rgba(60, 40, 30, 0.18);
  }
  * { margin: 0; padding: 0; box-sizing: border-box; }
  html, body {
    width: 1200px;
    height: 1200px;
    overflow: hidden;
    background: var(--page);
  }
  .stage {
    width: 1200px;
    height: 1200px;
    display: flex;
    align-items: center;
    justify-content: center;
  }
  .cover {
    position: relative;
    width: 900px;
    height: 900px;
    overflow: hidden;
    box-shadow: 0 6px 18px var(--shadow);
  }
  .cover-photo {
    position: absolute;
    inset: 0;
    background:
      radial-gradient(ellipse 32% 30% at 52% 62%, var(--hair-glow) 0%, rgba(181,86,42,0) 100%),
      radial-gradient(ellipse 90% 30% at 50% 100%, var(--cloud-bright) 0%, var(--cloud) 55%, rgba(217,217,239,0) 100%),
      radial-gradient(ellipse 30% 25% at 45% 6%, var(--sky) 0%, rgba(230,207,208,0) 100%),
      linear-gradient(180deg, var(--forest-high) 0%, var(--forest-mid) 45%, var(--road) 72%, var(--cloud) 100%);
  }
  .artist-name {
    position: absolute;
    top: 90px;
    left: 44px;
    right: 0;
    text-align: center;
    font-family: "Nunito Sans", sans-serif;
    font-weight: 400;
    font-size: 190px;
    line-height: 1;
    letter-spacing: 0.08em;
    color: var(--ink-light);
    text-transform: uppercase;
  }
  .song-title {
    position: absolute;
    top: 802px;
    left: 0;
    right: 0;
    text-align: center;
    font-family: "Nunito Sans", sans-serif;
    font-weight: 400;
    font-size: 44px;
    line-height: 1;
    letter-spacing: 0.08em;
    color: var(--ink-light);
    text-transform: uppercase;
  }
</style>
</head>
<body>
  <main class="stage">
    <section class="cover">
      <div class="cover-photo" role="img" aria-label="Photograph: two friends with long red hair embracing, seen from behind, on an autumn forest road with soft white clouds rising around them"></div>
      <h1 class="artist-name">TOVA</h1>
      <p class="song-title">Stars over harbour</p>
    </section>
  </main>
</body>
</html>
```